Need Bold, Hip Card for Concert Ticket Website Gleaming Passes!

Hi there! I am putting together a business/website that sells event tickets (mostly concerts, but also some sports and theater). Think SeatNook, but much smaller. The site is called Gleaming Passes. I have a new logo (attached, with black/red/white color scheme), and am looking for a modern/cool/original business card design. Note that I am thinking of having the card itself in the shape of a ticket (die cut), so you may want to keep that in mind when designing, but I'm not set on that. I'm also open to alternative card sizes, thicknesses, glossy, spot UV, etc. in order to stand out. I'm attaching a potential die cut template and a sample card using that template in case you want to work with that.
Target Market(s)
Music fans, people that like going to see live events
Industry/Entity Type
Entertainment
Contact Information for Business Card
Information that I'd like to have:
website address - www.gleamingpasses.example
phone number: 1-833-5GLEAMNG (532-6264)
my name - Wendel Pike

```html
<!DOCTYPE html>
<html lang="en">
<head>
<meta charset="utf-8">
<title>Gleaming Passes — Business Card</title>
<link href="https://fonts.googleapis.com/css2?family=Montserrat:wght@400;700&display=swap" rel="stylesheet">
<style>
  :root {
    --stage: #3a0407;
    --card-red: #9a0309;
    --card-black: #050505;
    --ink-dark: #0c0c0c;
    --ink-light: #ffffff;
    --ink-soft: #f1dede;
  }
  * { box-sizing: border-box; margin: 0; padding: 0; }
  html, body { width: 1200px; height: 800px; overflow: hidden; }
  body {
    background: var(--stage);
    font-family: "Montserrat", sans-serif;
    position: relative;
  }
  .card {
    position: absolute;
    top: 257px;
    width: 500px;
    height: 286px;
  }
  .card--front { left: 70px; }
  .card--back { left: 630px; }
  .card__shape { position: absolute; inset: 0; width: 500px; height: 286px; }
  .card--front .card__shape path { fill: var(--card-red); }
  .card--back .card__shape path { fill: var(--card-black); }

  .holder { position: absolute; left: 80px; top: 40px; color: var(--ink-light); }
  .holder__name { font-weight: 700; font-size: 17px; letter-spacing: 0.2px; }
  .holder__role { font-weight: 400; font-size: 12px; color: var(--ink-soft); margin-top: 2px; }

  .contact {
    position: absolute; left: 80px; top: 168px;
    list-style: none; color: var(--ink-light);
    font-size: 12.5px; font-weight: 400;
  }
  .contact__item { display: flex; align-items: center; gap: 10px; margin-bottom: 12px; white-space: nowrap; }
  .contact__icon { width: 12px; height: 12px; flex: none; }
  .contact__icon * { fill: none; stroke: var(--ink-soft); stroke-width: 1.4; }

  .brand-symbol-area {
    position: absolute; left: 330px; top: 62px;
    width: 110px; height: 170px;
    background: var(--ink-dark);
  }

  .wordmark {
    position: absolute; inset: 0;
    display: flex; align-items: center; justify-content: center;
  }
  .wordmark__name {
    color: var(--ink-light);
    font-weight: 700; font-size: 32px;
    letter-spacing: 0.5px;
  }
</style>
</head>
<body>
  <section class="card card--front" aria-label="Card front">
    <svg class="card__shape" viewBox="0 0 500 286" aria-hidden="true">
      <path d="M0 0 H500 V97 A46 46 0 0 0 500 189 V286 H0 V189 A46 46 0 0 0 0 97 Z"/>
    </svg>
    <div class="holder">
      <p class="holder__name">Wendel Pike</p>
      <p class="holder__role">Owner</p>
    </div>
    <ul class="contact">
      <li class="contact__item">
        <svg class="contact__icon" viewBox="0 0 12 12" aria-hidden="true"><rect x="3" y="0.7" width="6" height="10.6" rx="1"/><line x1="5" y1="9.3" x2="7" y2="9.3"/></svg>
        1-833-5GLEAMNG (532-6264)
      </li>
      <li class="contact__item">
        <svg class="contact__icon" viewBox="0 0 12 12" aria-hidden="true"><rect x="0.7" y="2.2" width="10.6" height="7.6"/><polyline points="0.7,2.2 6,6.6 11.3,2.2"/></svg>
        info@gleamingpasses.example
      </li>
      <li class="contact__item">
        <svg class="contact__icon" viewBox="0 0 12 12" aria-hidden="true"><circle cx="6" cy="6" r="5.2"/><ellipse cx="6" cy="6" rx="2.2" ry="5.2"/><line x1="0.8" y1="6" x2="11.2" y2="6"/></svg>
        www.gleamingpasses.example
      </li>
    </ul>
    <div class="brand-symbol-area" role="img" aria-label="Large brand ticket symbol decoration"></div>
  </section>

  <section class="card card--back" aria-label="Card back">
    <svg class="card__shape" viewBox="0 0 500 286" aria-hidden="true">
      <path d="M0 0 H500 V97 A46 46 0 0 0 500 189 V286 H0 V189 A46 46 0 0 0 0 97 Z"/>
    </svg>
    <div class="wordmark">
      <p class="wordmark__name">Gleaming Passes</p>
    </div>
  </section>
</body>
</html>
```